Tallowfern Studio business cards

We are a new company based in New Zealand. We Specialize in High end Luxury Residential Architecture.

Every home is bespoke and is designed to each clients individual requirements and needs.

I like to design buildings that inspire people through light and form while offering a high level of comfort and usability.

Lines of sight, proportion and balance are fundamental to the spaces I create.
Updates

August 5th is current deadline - Today's date is the 13th of August.

Target Market(s)

New Zealanders who want a custom individual home design, typically 30-65 year old males and females

Industry/Entity Type

Architecture

Contact Information for Business Card

Director - Derek Holloway
Contact Number - 0274619037
Email - info@tallowfernstudio.co.nz
Webstie - www.tallowfernstudio.co.nz
Social Media - @tallowfernstudio

Font styles to use
Sans Serif

Requirements
Must have
• Logo (Both Sides)
Website
Email
Contact Number
Social Media

Nice to have
• Texture
Should not have
• More than 3 colours - typically I would've thought 2 would be good to match the logo.

```html
<!DOCTYPE html>
<html lang="en">
<head>
<meta charset="utf-8">
<title>Tallowfern Studio – Business Cards</title>
<link href="https://fonts.googleapis.com/css2?family=Josefin+Sans:wght@300;400&family=Montserrat:wght@700&display=swap" rel="stylesheet">
<style>
  :root {
    --ink: #000000;
    --paper: #ffffff;
    --card-shadow: rgba(0,0,0,0.28);
  }
  * { margin: 0; padding: 0; box-sizing: border-box; }
  html, body { width: 1200px; height: 1200px; overflow: hidden; background: var(--paper); }
  .canvas { position: relative; width: 1200px; height: 1200px; background: var(--paper); overflow: hidden; }

  .card { position: absolute; left: 203px; width: 657px; height: 385px; }
  .card--front { top: 134px; background: var(--ink); color: var(--paper); }
  .card--back { top: 619px; left: 198px; background: var(--paper); color: var(--ink);
    box-shadow: 0 4px 4px var(--card-shadow); }

  .brand-mark { position: absolute; display: block; }
  .wordmark { position: absolute; font-family: "Josefin Sans", sans-serif; font-weight: 400;
    text-align: center; white-space: nowrap; line-height: 1; }
  .wordmark__name, .wordmark__sub { display: block; }
  .wordmark__name span, .wordmark__sub span { display: inline-block; }

  .card--front .brand-mark { left: 286px; top: 99px; }
  .card--front .wordmark { left: 124px; top: 232px; width: 410px; }
  .card--front .wordmark__name span { font-size: 38px; letter-spacing: 17px; margin-right: -17px; }
  .card--front .wordmark__sub { margin-top: 14px; }
  .card--front .wordmark__sub span { font-size: 13px; letter-spacing: 71px; margin-right: -71px; }

  .back-mark { position: absolute; left: 0; width: 100%; top: 62px; text-align: center; }
  .back-mark svg { display: block; margin: 0 auto; }
  .back-mark__name { display: block; margin-top: 6px; font-family: "Josefin Sans", sans-serif;
    font-weight: 400; font-size: 10px; letter-spacing: 4px; padding-left: 4px; line-height: 1; }

  .person { position: absolute; left: 0; width: 100%; text-align: center; }
  .person__name { top: 124px; font-family: "Montserrat", sans-serif; font-weight: 700;
    font-size: 18px; letter-spacing: 5px; padding-left: 5px; line-height: 1; }
  .person__role { top: 157px; font-family: "Josefin Sans", sans-serif; font-weight: 300;
    font-size: 16px; letter-spacing: 3.5px; padding-left: 3.5px; line-height: 1; }
  .divider-dot { position: absolute; left: 322px; top: 201px; width: 13px; height: 13px;
    border-radius: 50%; background: var(--ink); }
  .contact { position: absolute; left: 0; width: 100%; top: 238px; text-align: center;
    font-family: "Josefin Sans", sans-serif; font-weight: 300; font-size: 21px; line-height: 24px;
    font-style: normal; }

  .lockup { position: absolute; left: 812px; top: 1014px; width: 360px; height: 180px; color: var(--ink); }
  .lockup .brand-mark { left: 141px; top: 0; }
  .lockup .wordmark { left: 0; top: 122px; width: 360px; }
  .lockup .wordmark__name span { font-size: 31px; letter-spacing: 15px; margin-right: -15px; }
  .lockup .wordmark__sub { margin-top: 10px; }
  .lockup .wordmark__sub span { font-size: 11px; letter-spacing: 63px; margin-right: -63px; }
</style>
</head>
<body>
<main class="canvas">

  <section class="card card--front" aria-label="Business card front">
    <svg class="brand-mark" width="84" height="84" viewBox="0 0 84 84" aria-hidden="true">
      <circle cx="42" cy="42" r="38" fill="none" stroke="var(--paper)" stroke-width="6"/>
    </svg>
    <div class="wordmark">
      <span class="wordmark__name"><span>TALLOWFERN</span></span>
      <span class="wordmark__sub"><span>STUDIO</span></span>
    </div>
  </section>

  <section class="card card--back" aria-label="Business card back">
    <div class="back-mark">
      <svg width="26" height="26" viewBox="0 0 26 26" aria-hidden="true">
        <circle cx="13" cy="13" r="11" fill="none" stroke="var(--ink)" stroke-width="3"/>
      </svg>
      <span class="back-mark__name">TALLOWFERN STUDIO</span>
    </div>
    <p class="person person__name">DEREK HOLLOWAY</p>
    <p class="person person__role">DIRECTOR</p>
    <span class="divider-dot" aria-hidden="true"></span>
    <address class="contact">
      0274619037 . info@tallowfernstudio.co.nz<br>
      www.tallowfernstudio.co.nz<br>
      Social Media @tallowfernstudio
    </address>
  </section>

  <section class="lockup" aria-label="Brand lockup">
    <svg class="brand-mark" width="78" height="78" viewBox="0 0 78 78" aria-hidden="true">
      <circle cx="39" cy="39" r="35" fill="none" stroke="var(--ink)" stroke-width="6"/>
    </svg>
    <div class="wordmark">
      <span class="wordmark__name"><span>TALLOWFERN</span></span>
      <span class="wordmark__sub"><span>STUDIO</span></span>
    </div>
  </section>

</main>
</body>
</html>
```